We want to revamp our current website -www.kelvoro-tek.com

We need to have a new website for our company that offers non-destructive and testing solutions around Africa. We have a current website but it does not fulfil our needs as it is:<br/>1. Not clear and bright<br/>2. Does not fit well in mobile <br/>3. Is not easily updatable by our staff. <br/>4. Is not linked to our social media sites.<br/>We would like to have a website that addresses the above issues. Our colours are Red and Blue and should communicate to our clients, that we are a professional company open for business, ready to solve their non-destructive testing problems around Africa. * Helpful if it is a wordpress website.

Target Market(s)

Our customers are B2B Corporate clients. We mainly work in
1. Storage Terminals
2. Refineries
3. Oil and Gas offshore and onshore rigs.

Industry/Entity Type

Oil And Gas

Contact Information for Business Card

Please find our current business card on the uploaded files.

Coding

Coded - Design and coding required

Number of Pages Required

5+ page

Font styles to use
Serif
Sans Serif

Requirements
Must have
• I like this site www.pirel-checkworks.com They are in the same industry.
• I don't understand how to call them but all the 'call to action' buttons, and links to our Social media pages.
• Must have a place where we update information in a regular basis. A Blog!

```html
<!DOCTYPE html>
<html lang="en">
<head>
<meta charset="utf-8">
<title>Kelvoro Engineering</title>
<link href="https://fonts.googleapis.com/css2?family=Poppins:wght@300;400;500;600&display=swap" rel="stylesheet">
<style>
:root{
  --red:#a5121d;
  --red-dark:#8c0f18;
  --navy:#1b2a5e;
  --ink:#1e1e1e;
  --muted:#555;
  --light:#f4f4f4;
  --footer:#151515;
  --white:#fff;
}
*{box-sizing:border-box;margin:0;padding:0}
html,body{width:1200px;height:3240px;overflow:hidden}
body{position:relative;font-family:'Poppins',sans-serif;color:var(--ink);background:var(--white)}
.abs{position:absolute}
.btn{position:absolute;display:flex;align-items:center;justify-content:center;gap:8px;border-radius:24px;color:var(--white);font-size:16px;font-weight:500;text-transform:uppercase}
.btn-red{background:var(--red)}
.btn-navy{background:var(--navy)}
.arrow{width:18px;height:10px}
/* header */
.topbar{left:0;top:0;width:1200px;height:50px;background:rgba(255,255,255,.85)}
.brand{left:111px;top:6px;width:138px;height:114px;border-radius:50%;background:var(--white);display:flex;align-items:center;justify-content:center;box-shadow:0 2px 6px rgba(0,0,0,.2)}
.brand span{font-size:20px;font-weight:600;color:var(--navy)}
.nav{left:322px;top:13px;display:flex;gap:20px;font-size:16px;font-weight:500}
.nav .active{color:var(--red)}
.flag{left:729px;top:9px;width:32px;height:32px;border-radius:50%;background:linear-gradient(135deg,#c8102e,#fff 50%,#012169)}
.caret{left:775px;top:22px;width:0;height:0;border:5px solid transparent;border-top-color:var(--red)}
.search{left:813px;top:7px;width:180px;height:37px;border:1px solid #aaa;border-radius:19px;font-size:14px;color:#777;padding:8px 15px}
.social-top{left:1020px;top:19px;display:flex;gap:12px}
.dot{width:12px;height:12px;border-radius:50%;background:var(--navy)}
/* hero */
.hero{left:0;top:0;width:1200px;height:613px;background:linear-gradient(180deg,#8b8f8c 0%,#6f6a5a 45%,#4e4638 100%)}
.hero-shade{left:0;top:0;width:1200px;height:613px;background:linear-gradient(90deg,rgba(40,40,40,.35),rgba(0,0,0,.1) 60%,rgba(150,180,40,.35))}
.hero-title{left:0;top:176px;width:1200px;text-align:center;color:var(--white);font-size:41px;font-weight:600}
.hero-sub{left:0;top:232px;width:1200px;text-align:center;color:var(--white);font-size:18px}
.hero-line{left:600px;top:325px;width:1px;height:68px;background:var(--red)}
.play{left:558px;top:392px;width:84px;height:84px}
.hero-call{left:111px;top:566px;color:var(--white);font-size:12.5px;letter-spacing:-.2px;white-space:nowrap}
.hero-phone{left:733px;top:559px;display:flex;align-items:center;gap:10px;color:var(--white);font-size:19px;font-weight:500}
.slides{left:1106px;top:262px;color:var(--white);font-size:20px;font-weight:500}
/* section heads */
.kicker{width:1200px;left:0;text-align:center;color:var(--navy);font-size:17px;font-weight:500}
.head{width:1200px;left:0;text-align:center;font-size:40px;font-weight:300;color:var(--ink)}
.head b{font-weight:600}
.about-deco{left:0;top:613px;width:400px;height:240px;background:linear-gradient(90deg,#eef0f3,rgba(255,255,255,0))}
.about-text{left:154px;top:771px;width:892px;text-align:justify;text-align-last:center;font-size:14px;line-height:28px;color:var(--muted)}
/* focus cards */
.frame{width:307px;height:370px;border:2px solid var(--navy);border-radius:6px}
.card{width:307px;height:369px;border-radius:8px;overflow:hidden}
.card-label{left:22px;bottom:30px;color:var(--white);font-size:17px;font-weight:500;line-height:26px;text-transform:uppercase;position:absolute}
/* what we do */
.wwd-tab{left:599px;top:1557px;width:601px;height:80px;background:var(--navy);border-top-left-radius:22px;color:var(--white);font-size:18px;letter-spacing:6px;padding:25px 40px;font-weight:500}
.wwd-left{left:0;top:1591px;width:600px;height:388px;background:linear-gradient(135deg,#5a6790,#3b4a78)}
.wwd-left-bar{left:0;top:1979px;width:600px;height:11px;background:var(--navy)}
.wwd-right{left:600px;top:1633px;width:600px;height:346px;background:linear-gradient(135deg,#a3353d,#b0252c 60%,#c14a45)}
.wwd-title{color:var(--white);font-size:25px;font-weight:600;text-transform:uppercase}
.wwd-text{color:var(--white);font-size:13.5px;line-height:28.5px;text-align:justify}
/* blogs */
.greyband{left:0;top:2348px;width:1200px;height:529px;background:var(--light)}
.post{width:307px;height:399px;background:var(--white);box-shadow:0 0 6px rgba(0,0,0,.12)}
.post-img{position:absolute;left:0;top:0;width:307px;height:186px}
.post-meta{position:absolute;left:8px;top:200px;width:291px;display:flex;justify-content:space-between;font-size:13px;color:var(--navy)}
.post-meta .c{color:#666}
.post-title{position:absolute;left:8px;top:231px;width:291px;font-size:18px;line-height:25px}
.post-text{position:absolute;left:8px;top:286px;width:291px;font-size:14px;line-height:24px;color:#666;text-align:justify}
.post-more{position:absolute;left:8px;top:366px;font-size:13px;color:var(--red);display:flex;align-items:center;gap:8px}
/* clients */
.client{top:2737px;width:190px;height:53px;background:var(--white);display:flex;align-items:center;justify-content:center;gap:8px;font-size:20px;font-weight:500;color:#3a3a3a}
.client i{width:14px;height:14px;background:#3a3a3a;border-radius:50%;display:block}
/* footer */
.footer{left:0;top:2877px;width:1200px;height:363px;background:var(--footer);color:var(--white)}
.f-head{font-size:16px;font-weight:600;text-transform:uppercase}
.f-links{font-size:14px;line-height:25.6px}
.f-contact{display:flex;gap:14px;font-size:14px;line-height:26px}
.f-icon{width:28px;height:28px;border:1px solid #ccc;border-radius:50%;flex:none;display:flex;align-items:center;justify-content:center;margin-top:8px}
.f-map{left:632px;top:103px;width:270px;height:156px;background:linear-gradient(135deg,#eef0ea,#e2e6dc)}
.f-social{left:995px;top:103px;display:flex;gap:14px}
.f-social span{width:22px;height:22px;border-radius:50%;background:var(--white)}
.copy{left:0;top:318px;width:1200px;text-align:center;font-size:14px;word-spacing:2px}
.copy span{margin:0 10px}
</style>
</head>
<body>

<!-- hero -->
<div class="abs hero" role="img" aria-label="Refinery towers at dusk with an engineer in a hard hat and high-visibility vest"></div>
<div class="abs hero-shade"></div>
<div class="abs topbar"></div>
<div class="abs brand"><span>KELVORO</span></div>
<nav class="abs nav"><span class="active">Home</span><span>About Us</span><span>Services</span><span>Blog</span><span>Contact Us</span></nav>
<div class="abs flag" role="img" aria-label="Language selector flag"></div>
<div class="abs caret"></div>
<div class="abs search">search
  <svg class="abs" style="right:14px;top:11px" width="13" height="13" viewBox="0 0 13 13"><circle cx="5.5" cy="5.5" r="4" fill="none" stroke="#777" stroke-width="2"/><line x1="8.5" y1="8.5" x2="12" y2="12" stroke="#777" stroke-width="2"/></svg>
</div>
<div class="abs social-top"><span class="dot"></span><span class="dot"></span><span class="dot"></span></div>

<h1 class="abs hero-title">KELVORO ENGINEERING</h1>
<p class="abs hero-sub">We offer inspection &amp; engineering services</p>
<div class="btn btn-red" style="left:517px;top:277px;width:167px;height:48px;font-size:16px">Get Started</div>
<div class="abs hero-line"></div>
<svg class="abs play" viewBox="0 0 84 84"><circle cx="42" cy="42" r="40" fill="rgba(255,255,255,.15)" stroke="#8a1a20" stroke-width="3"/><circle cx="42" cy="42" r="26" fill="none" stroke="#fff" stroke-width="2"/><path d="M36 32 L52 42 L36 52 Z" fill="#fff"/></svg>
<div class="abs slides">
  <svg width="70" height="80" viewBox="0 0 70 80"><line x1="5" y1="12" x2="20" y2="12" stroke="#fff"/><circle cx="5" cy="12" r="5" fill="#fff"/><circle cx="5" cy="30" r="3" fill="rgba(255,255,255,.6)"/><circle cx="5" cy="46" r="3" fill="rgba(255,255,255,.6)"/><circle cx="5" cy="62" r="3" fill="rgba(255,255,255,.6)"/></svg>
  <span class="abs" style="left:32px;top:0">01</span>
</div>
<p class="abs hero-call">Don’t Let Technology Issues Plague Your Business.&nbsp; We’re Here to Help – GIVE US A CALL TODAY!</p>
<div class="abs hero-phone">
  <svg width="32" height="32" viewBox="0 0 32 32"><circle cx="16" cy="16" r="14" fill="none" stroke="var(--red)" stroke-width="2"/><path d="M11 9c-2 2-1 6 3 10s8 5 10 3l-3-3-2 2c-2-1-4-3-5-5l2-2z" fill="var(--red)"/></svg>
  + 254 20 418 3302/3
</div>
<svg class="abs" style="left:1066px;top:551px" width="22" height="45" viewBox="0 0 22 45"><rect x="1" y="1" width="20" height="28" rx="10" fill="none" stroke="#fff" stroke-width="1.5"/><line x1="11" y1="7" x2="11" y2="13" stroke="#fff" stroke-width="1.5"/><path d="M6 34 L11 38 L16 34 M6 39 L11 43 L16 39" fill="none" stroke="#fff"/></svg>

<!-- about -->
<div class="abs about-deco" role="img" aria-label="Faint line drawing of plant piping"></div>
<p class="abs kicker" style="top:692px">Company</p>
<h2 class="abs head" style="top:712px"><b>About</b> Kelvoro</h2>
<p class="abs about-text">With roots in the coast, we have over 15 years’ experience in NDT, Mechanical engineering and Marine services. We enjoy a regional presence in The larger Eastern and Central African Region. Though our head office is located on the coast of Kenya, with a fully fledged testing laboratory not far from our office. We provide testing services across various countries in Africa.</p>
<div class="btn btn-red" style="left:517px;top:871px;width:166px;height:47px">Read More <svg class="arrow" viewBox="0 0 18 10"><path d="M0 5h14M11 1l5 4-5 4" stroke="#fff" stroke-width="2" fill="none"/></svg></div>

<!-- focus areas -->
<p class="abs kicker" style="top:1000px">Solutions</p>
<h2 class="abs head" style="top:1020px"><b>Our</b> Focus Areas</h2>
<div class="abs frame" style="left:102px;top:1093px"></div>
<div class="abs frame" style="left:437px;top:1093px"></div>
<div class="abs frame" style="left:771px;top:1093px"></div>
<div class="abs card" style="left:111px;top:1102px;background:linear-gradient(160deg,#9fb3d8,#8a8f98 40%,#3a3d42)" role="img" aria-label="Large steel storage tank with a spiral staircase">
  <span class="card-label">Storage Terminals</span></div>
<div class="abs card" style="left:446px;top:1102px;background:linear-gradient(180deg,#2a3040,#4a5060 45%,#6a5a2a 70%,#1e2418)" role="img" aria-label="Refinery tanks lit up at night">
  <span class="card-label">Refineries</span></div>
<div class="abs card" style="left:780px;top:1102px;background:linear-gradient(180deg,#c7cfd6,#8a6d55 55%,#4b3a2c)" role="img" aria-label="Pipework and valves at a gas installation">
  <span class="card-label">Oil and Gas Offshore &amp;<br>Onshore Rigs.</span></div>

<!-- what we do -->
<div class="abs wwd-left" role="img" aria-label="Inspector in protective gear testing pipework"></div>
<div class="abs wwd-left-bar"></div>
<div class="abs wwd-right" role="img" aria-label="Engineer welding steel flanges"></div>
<div class="abs wwd-tab">WHAT WE DO</div>
<h3 class="abs wwd-title" style="left:110px;top:1690px">Kelvoro Inspection</h3>
<p class="abs wwd-text" style="left:111px;top:1733px;width:428px">The Inspection and NDT Division has the technical capability, backed by the right equipment to provide full range NDT solutions in accordance with client requirements and in compliance with local and international standards</p>
<div class="btn btn-red" style="left:111px;top:1862px;width:182px;height:46px">View Services <svg class="arrow" viewBox="0 0 18 10"><path d="M0 5h14M11 1l5 4-5 4" stroke="#fff" stroke-width="2" fill="none"/></svg></div>
<h3 class="abs wwd-title" style="left:657px;top:1690px">Kelvoro&nbsp; Engineering</h3>
<p class="abs wwd-text" style="left:660px;top:1733px;width:428px">Our Mechanical Engineering division is majorly involved with ASME compliant steel fabrication and welding both at our workshop and on client sites. With our corporate culture of qulity, we have engaged a team of well specialized techicians</p>
<div class="btn btn-navy" style="left:660px;top:1862px;width:182px;height:46px">View Services <svg class="arrow" viewBox="0 0 18 10"><path d="M0 5h14M11 1l5 4-5 4" stroke="#fff" stroke-width="2" fill="none"/></svg></div>

<!-- blogs -->
<div class="abs greyband"></div>
<p class="abs kicker" style="top:2071px">Latest From</p>
<h2 class="abs head" style="top:2091px"><b>Our</b> Blogs</h2>

<article class="abs post" style="left:111px;top:2164px">
  <div class="post-img" style="background:linear-gradient(160deg,#8a6e62,#c4552e 50%,#6a4a3e)" role="img" aria-label="Technician in orange overalls working on a steel surface"></div>
  <div class="post-meta"><span>▦6,April 2019</span><span class="c">○ 0 Comments</span></div>
  <h4 class="post-title" style="font-weight:400">Lorem , consectetur adipiscing , sed do eiusmod</h4>
  <p class="post-text">Lorem ipsum dolor sit amet, consectetur adipiscing elit, sed do eiusmod tempor incididunt ut labore et</p>
  <a class="post-more">READ MORE <svg width="14" height="8" viewBox="0 0 14 8"><path d="M0 4h11M8 1l4 3-4 3" stroke="var(--red)" stroke-width="1.6" fill="none"/></svg></a>
</article>
<article class="abs post" style="left:446px;top:2164px">
  <div class="post-img" style="background:linear-gradient(150deg,#6e7a8c,#2e4a7a 45%,#5a5a50)" role="img" aria-label="Workers inspecting a large blue pipeline"></div>
  <div class="post-meta"><span>▦1,Feb 20120</span><span class="c">○ 0 Comments</span></div>
  <h4 class="post-title" style="font-weight:400">Lorem , consectetur adipiscing , sed do eiusmod</h4>
  <p class="post-text">Lorem ipsum dolor sit amet, consectetur adipiscing elit, sed do eiusmod tempor incididunt ut labore et</p>
  <a class="post-more">READ MORE <svg width="14" height="8" viewBox="0 0 14 8"><path d="M0 4h11M8 1l4 3-4 3" stroke="var(--red)" stroke-width="1.6" fill="none"/></svg></a>
</article>
<article class="abs post" style="left:781px;top:2164px">
  <div class="post-img" style="background:linear-gradient(160deg,#7a5a4a,#4a4a4a 50%,#8a7a6a)" role="img" aria-label="Technician taking a sample beside test equipment"></div>
  <div class="post-meta"><span>▦25,Mar 2015</span><span class="c">○ 0 Comments</span></div>
  <h4 class="post-title" style="font-weight:400">Lorem , consectetur adipiscing , sed do eiusmod</h4>
  <p class="post-text">Lorem ipsum dolor sit amet, consectetur adipiscing elit, sed do eiusmod tempor incididunt ut labore et</p>
  <a class="post-more">READ MORE <svg width="14" height="8" viewBox="0 0 14 8"><path d="M0 4h11M8 1l4 3-4 3" stroke="var(--red)" stroke-width="1.6" fill="none"/></svg></a>
</article>

<!-- clients -->
<p class="abs kicker" style="top:2646px">Our Trust</p>
<h2 class="abs head" style="top:2666px"><b>Our</b> Clients</h2>
<div class="abs client" style="left:111px"><i></i>Harbrook</div>
<div class="abs client" style="left:308px">Velmora</div>
<div class="abs client" style="left:505px">Tansel Logistics</div>
<div class="abs client" style="left:702px"><i></i>Qalden Energy</div>
<div class="abs client" style="left:899px">Ostrava Power</div>

<!-- footer -->
<footer class="abs footer">
  <h5 class="abs f-head" style="left:111px;top:64px">Quick Link</h5>
  <ul class="abs f-links" style="left:111px;top:93px;list-style:none">
    <li>Home</li><li>About</li><li>Services</li><li>Locations</li><li>Careers</li><li>Blogs</li><li>Contcat us</li>
  </ul>
  <h5 class="abs f-head" style="left:299px;top:64px">Contact Details</h5>
  <div class="abs f-contact" style="left:294px;top:93px">
    <span class="f-icon"><svg width="12" height="14" viewBox="0 0 12 14"><path d="M6 13C2 8 1 6 1 5a5 5 0 0 1 10 0c0 1-1 3-5 8z" fill="none" stroke="#fff" stroke-width="1.3"/><circle cx="6" cy="5" r="1.6" fill="#fff"/></svg></span>
    <span>Kelvoro Engineering<br>Tiwari Lane, Coastline</span>
  </div>
  <div class="abs f-contact" style="left:294px;top:161px">
    <span class="f-icon"><svg width="12" height="12" viewBox="0 0 12 12"><path d="M3 1C1 2 1 5 4 8s6 3 7 1L9 7 7.5 8.3C6 7.5 4.5 6 3.7 4.5L5 3z" fill="#fff"/></svg></span>
    <span>PHONE<br>254 20 418 3302/3</span>
  </div>
  <div class="abs f-contact" style="left:294px;top:229px">
    <span class="f-icon"><svg width="13" height="10" viewBox="0 0 13 10"><rect x=".7" y=".7" width="11.6" height="8.6" rx="1" fill="none" stroke="#fff" stroke-width="1.2"/><path d="M1 1l5.5 4.5L12 1" fill="none" stroke="#fff" stroke-width="1.2"/></svg></span>
    <span>EMAIL<br>&nbsp;info@kelvoro-tek.com</span>
  </div>
  <h5 class="abs f-head" style="left:632px;top:64px">Location Map</h5>
  <div class="abs f-map" role="img" aria-label="Street map marking the office location"></div>
  <h5 class="abs f-head" style="left:995px;top:64px">Follow Us</h5>
  <div class="abs f-social"><span></span><span></span><span></span></div>
  <p class="abs copy"><span>Copyright © 2020. All Rights Reserved</span><span>Terms of Use</span><span>Privacy Policy</span></p>
</footer>

</body>
</html>
```